A business selling natural soaps online and in farmers markets. I want it to reflect local commerce and natural lifestyle. My colors are olive green and saddle brown. I want the dimensions to be 2.25 x 3.25" with matte finish.
Updates

The name of my company is Fern Hollow Soapworks, LLC

Industry/Entity Type

Business

```html
<!DOCTYPE html>
<html lang="en">
<head>
<meta charset="utf-8">
<title>Fern Hollow Soapworks, LLC — Card</title>
<link rel="stylesheet" href="https://fonts.googleapis.com/css2?family=Lancelot&display=swap">
<style>
  :root {
    --wood-dark: #6a3a22;
    --wood-mid: #9c603c;
    --wood-light: #c79a76;
    --leaf-green: rgba(118, 176, 58, 0.86);
    --cream: #fbf8ef;
    --ink: #111111;
  }
  * { margin: 0; padding: 0; box-sizing: border-box; }
  html, body {
    width: 1200px;
    height: 837px;
    overflow: hidden;
    background: #ffffff;
  }
  .card {
    position: relative;
    width: 1200px;
    height: 837px;
    overflow: hidden;
    font-family: "Lancelot", serif;
  }
  .wood-backdrop {
    position: absolute;
    inset: 0;
    background:
      linear-gradient(160deg, rgba(255,255,255,0.12) 0%, rgba(0,0,0,0) 40%, rgba(0,0,0,0.18) 100%),
      linear-gradient(100deg, var(--wood-light) 0%, var(--wood-mid) 45%, var(--wood-dark) 100%);
  }
  .business-name {
    position: absolute;
    left: 90px;
    top: 120px;
    width: 700px;
    text-align: center;
    color: var(--cream);
    font-family: "Lancelot", serif;
    font-size: 62px;
    line-height: 1;
    white-space: nowrap;
  }
  .headline-panel {
    position: absolute;
    left: 200px;
    top: 357px;
    width: 815px;
    height: 258px;
    background: var(--leaf-green);
    display: flex;
    flex-direction: column;
    justify-content: center;
    align-items: center;
    color: #ffffff;
    font-size: 104px;
    line-height: 1.04;
    white-space: nowrap;
  }
  .scent-list {
    position: absolute;
    left: 160px;
    width: 895px;
    top: 620px;
    text-align: center;
    color: #ffffff;
    font-size: 46px;
    line-height: 1.2;
    white-space: nowrap;
  }
  .scent-note {
    position: absolute;
    left: 160px;
    width: 895px;
    top: 682px;
    text-align: center;
    color: #ffffff;
    font-size: 38px;
    line-height: 1.2;
    white-space: nowrap;
  }
  .contact-email {
    position: absolute;
    left: 1135px;
    top: 423px;
    transform: translate(-50%, -50%) rotate(-90deg);
    white-space: nowrap;
    color: var(--ink);
    font-family: Arial, Helvetica, sans-serif;
    font-size: 49px;
  }
</style>
</head>
<body>
  <main class="card">
    <div class="wood-backdrop" role="img" aria-label="Photograph of warm brown wooden planks"></div>

    <p class="business-name">Fern Hollow Soapworks, LLC</p>

    <section class="headline-panel">
      <p>Natural Handmade</p>
      <p>Moisturizing Soaps..</p>
    </section>

    <p class="scent-list">Cider - Cocoa Butter - Lavendar - Christmas</p>
    <p class="scent-note">plus more, just ask us!</p>

    <p class="contact-email">info@fernhollowsoapworks.com</p>
  </main>
</body>
</html>
```